Marlow Fields Thank-You Tag

Looking for a file that incorporates current branding/colors and says:

"Thanks for Swimming with Us!"
Marlow Fields Otters

Samples of other pieces we've done recently are attached.

Will be printed on cardstock that is
Width: 3.5 inches
Height: 2.5 inches

```html
<!DOCTYPE html>
<html lang="en">
<head>
<meta charset="utf-8">
<title>Marlow Fields Otters – Thank-You Tag</title>
<link href="https://fonts.googleapis.com/css2?family=Anton&family=Poppins:wght@600;700;800&family=Sacramento&display=swap" rel="stylesheet">
<style>
  :root{
    --stage:#d3d3d3;
    --navy-top:#244ea8;
    --navy-1:#1f43a3;
    --navy-2:#1b38a0;
    --navy-3:#1a3594;
    --navy-4:#1a3384;
    --wave-edge:#9aa8c8;
    --wave-band:#5b80cc;
    --pool:#6791c0;
    --white:#f5f7fb;
    --pink:#ef5fa0;
  }
  *{box-sizing:border-box;margin:0;padding:0}
  html,body{width:791px;height:1200px;overflow:hidden;background:var(--stage)}
  .tag{
    position:absolute;left:96px;width:606px;height:433px;overflow:hidden;
    box-shadow:14px 16px 18px rgba(0,0,0,.22);
  }
  .tag--front{top:105px}
  .tag--back{top:648px}
  .tag__scene{position:absolute;inset:0;width:606px;height:433px}
  .tag__frame{
    position:absolute;left:32px;top:31px;width:540px;height:400px;
    border:2px dotted var(--white);border-bottom:none;
  }
  .mascot{
    position:absolute;left:461px;top:287px;width:84px;height:74px;
    background:var(--white);border-radius:60% 40% 50% 50%;opacity:.92;
  }
  /* front */
  .year{position:absolute;font-family:"Poppins",sans-serif;font-weight:800;line-height:1}
  .year__twenty{left:185px;top:40px;font-size:160px;color:var(--white);letter-spacing:-4px}
  .year__ring{position:absolute;left:277px;top:65px;width:120px;height:120px;border-radius:50%;background:var(--white)}
  .year__badge{position:absolute;left:20px;top:20px;width:80px;height:80px;border-radius:50%;background:var(--navy-top);
    display:flex;align-items:center;justify-content:center;text-align:center;
    font-family:"Poppins",sans-serif;font-weight:700;font-size:11px;line-height:1.15;color:var(--white)}
  .year__twentysix{left:222px;top:160px;font-size:172px;color:var(--pink);letter-spacing:-6px}
  /* back */
  .thanks{position:absolute;left:0;width:606px;text-align:center;line-height:1}
  .thanks__lead{top:66px;font-family:"Anton",sans-serif;font-size:58px;color:var(--white)}
  .thanks__main{top:128px;font-family:"Anton",sans-serif;font-size:84px;color:var(--pink);letter-spacing:-1px}
  .thanks__script{top:160px;font-family:"Sacramento",cursive;font-size:72px;color:var(--white)}
  .thanks__team{top:240px;display:flex;align-items:center;justify-content:center;gap:8px;
    font-family:"Poppins",sans-serif;font-weight:700;font-size:25px;color:var(--white)}
  .thanks__rule{width:22px;height:2px;background:var(--pink)}
  .splash{position:absolute;top:132px;width:28px;height:30px;background:var(--white);border-radius:50% 50% 10% 50%;opacity:.9}
  .splash--left{left:80px}
  .splash--right{left:498px;transform:scaleX(-1)}
</style>
</head>
<body>

<svg width="0" height="0" style="position:absolute" aria-hidden="true">
  <symbol id="pool-scene" viewBox="0 0 606 433">
    <rect width="606" height="433" fill="var(--navy-top)"/>
    <path d="M0 100 C80 80 150 110 230 90 S380 120 450 100 S560 110 606 95 V433 H0Z" fill="var(--navy-1)"/>
    <path d="M0 150 C90 130 170 165 260 140 S420 170 500 150 S580 155 606 148 V433 H0Z" fill="var(--navy-2)"/>
    <path d="M0 210 C100 190 190 225 290 200 S440 230 520 210 S590 212 606 206 V433 H0Z" fill="var(--navy-3)"/>
    <path d="M0 265 C100 250 200 280 300 258 S460 285 540 268 L606 262 V433 H0Z" fill="var(--navy-4)"/>
    <path d="M0 312 C40 322 90 325 130 318 C180 308 220 298 260 306 C300 314 315 345 340 345 C370 345 395 300 430 306 C470 314 500 360 545 358 C575 356 595 345 606 336 V433 H0Z" fill="var(--wave-edge)"/>
    <path d="M0 317 C40 327 90 330 130 323 C180 313 220 303 260 311 C300 319 315 350 340 350 C370 350 395 305 430 311 C470 319 500 365 545 363 C575 361 595 350 606 341 V433 H0Z" fill="var(--wave-band)"/>
    <path d="M0 345 C50 350 100 345 140 338 C190 330 230 325 265 335 C300 345 320 372 345 372 C375 372 400 335 435 340 C475 346 505 385 548 382 C578 380 596 372 606 366 V433 H0Z" fill="var(--pool)"/>
  </symbol>
</svg>

<section class="tag tag--front">
  <svg class="tag__scene" aria-hidden="true"><use href="#pool-scene"/></svg>
  <div class="tag__frame"></div>
  <div class="year year__twenty">2</div>
  <div class="year__ring"><div class="year__badge">Marlow<br>Fields</div></div>
  <div class="year year__twentysix">26</div>
  <div class="mascot" role="img" aria-label="Leaping otter illustration"></div>
</section>

<section class="tag tag--back">
  <svg class="tag__scene" aria-hidden="true"><use href="#pool-scene"/></svg>
  <div class="tag__frame"></div>
  <h1 class="thanks thanks__lead">THANKS FOR</h1>
  <div class="splash splash--left" role="img" aria-label="Water splash ornament"></div>
  <div class="splash splash--right" role="img" aria-label="Water splash ornament"></div>
  <p class="thanks thanks__main">SWIMMING</p>
  <p class="thanks thanks__script">With Us</p>
  <p class="thanks thanks__team"><span class="thanks__rule"></span>Marlow Fields Otters<span class="thanks__rule"></span></p>
  <div class="mascot" role="img" aria-label="Leaping otter illustration"></div>
</section>

</body>
</html>
```